Flyer-Design für Aktionstag einer Teddy-Klinik gesucht
Zielgruppe
Ursprünglich ist die Teddyklinik Harvelsund eine Idee aus Schweden, doch inzwischen haben Fach-schaften in Deutschland an vielen medizinischen Universitäten diese Idee aufgenommen und umgesetzt. Seit einigen Jahren gibt es die Teddyklinik Harvelsund auch an der Universität zu Harvelsund, als AG der Fachschaft Medizin.
Aufgabenstellung
siehe Briefing-Dokument

```html
<!DOCTYPE html>
<html lang="de">
<head>
<meta charset="utf-8">
<title>Aktionstag Teddyklinik</title>
<link href="https://fonts.googleapis.com/css2?family=Arimo:wght@400;700&display=swap" rel="stylesheet">
<style>
  :root {
    --cyan: #00a6e6;
    --pink: #e5178f;
    --white: #ffffff;
    --ink: #3a3430;
    --bear-light: #d9cfc4;
    --bear-dark: #9a5a2c;
    --bear-mid: #a7773f;
  }
  * { margin: 0; padding: 0; box-sizing: border-box; }
  html, body { width: 1200px; height: 2408px; overflow: hidden; background: var(--white); }
  .flyer {
    position: relative; width: 1200px; height: 2408px; overflow: hidden;
    background: var(--white); font-family: "Arimo", Arial, sans-serif;
  }
  .hero-photo {
    position: absolute; left: 126px; top: 240px; width: 1050px; height: 720px;
    background: radial-gradient(ellipse at 30% 50%, var(--bear-light) 0 30%, transparent 55%),
                radial-gradient(ellipse at 65% 45%, var(--bear-dark) 0 30%, transparent 58%);
  }
  .title-main {
    position: absolute; left: 228px; top: 80px;
    font-weight: 700; font-size: 134px; line-height: 1; color: var(--cyan); letter-spacing: 1px;
  }
  .title-side {
    position: absolute; left: 1162px; top: 80px;
    transform-origin: 0 0; transform: rotate(90deg);
    font-weight: 700; font-size: 236px; line-height: 1; color: var(--cyan); letter-spacing: -6px;
    white-space: nowrap;
  }
  .shapes { position: absolute; left: 0; top: 0; }
  .panel-text {
    position: absolute; width: 1200px; text-align: center;
    color: var(--white); font-size: 40px; line-height: 1.38;
  }
  .intro { top: 1080px; left: -10px; transform: rotate(-4deg); }
  .intro strong { font-weight: 700; }
  .event {
    position: absolute; left: -30px; top: 1385px; width: 1200px; text-align: center;
    transform: rotate(-3deg); color: var(--pink);
  }
  .event-date { font-weight: 700; font-size: 76px; line-height: 1.1; }
  .event-time { font-weight: 700; font-size: 40px; margin-top: 8px; }
  .event-place { font-size: 42px; line-height: 1.3; margin-top: 34px; }
  .facts { top: 1775px; left: 62px; transform: rotate(-4deg); font-size: 40px; line-height: 1.4; }
  .footer-illustration {
    position: absolute; left: 116px; top: 2070px; width: 200px; height: 230px;
    border-radius: 50% 50% 40% 40%;
    background: radial-gradient(circle at 50% 45%, var(--bear-mid), #c9a27a 70%, transparent 72%);
  }
  .footer-name {
    position: absolute; left: 118px; top: 2318px;
    font-size: 24px; font-weight: 400; color: var(--ink);
  }
  .web { position: absolute; left: 452px; top: 2195px; font-size: 38px; color: var(--cyan); }
</style>
</head>
<body>
<main class="flyer">
  <div class="hero-photo" role="img" aria-label="Foto: zwei Teddybären mit Stethoskop und Pflastern"></div>

  <div class="title-main">AKTIONS</div>
  <div class="title-side">TAG</div>

  <svg class="shapes" width="1200" height="2408" viewBox="0 0 1200 2408" aria-hidden="true">
    <path fill="var(--pink)" d="M63 988 C150 960 250 1000 360 965 C480 925 600 935 720 912 C840 890 960 905 1061 893 L1064 1490 L1075 1500 L983 1500 L983 1328 L126 1397 Z"/>
    <path fill="var(--pink)" d="M168 1734 L983 1713 L983 1675 L1061 1668 L1145 2034 L227 1965 Z"/>
  </svg>

  <p class="panel-text intro">Am <strong>Aktionstag</strong> werden wir die<br>Lieblingsstofftiere der Kinder<br>„behandeln“ und sie als TeddyEltern<br>mit in alle Abläufe einbeziehen.</p>

  <div class="event">
    <div class="event-date">22.6.2019</div>
    <div class="event-time">10:00 - 16:00 Uhr</div>
    <div class="event-place">Marktplatz am Rathaus<br>in Harvelsund</div>
  </div>

  <p class="panel-text facts">Kinder aller Altersklassen sind willkommen<br>Kosten: Die Teilnahme ist kostenlos<br>Anmeldung: Keine Voranmeldung nötig</p>

  <div class="footer-illustration" role="img" aria-label="Illustration: Teddybär mit Stethoskop"></div>
  <div class="footer-name">Teddyklinik Harvelsund</div>

  <div class="web">www.teddyklinik.uni-harvelsund.de/</div>
</main>
</body>
</html>
```